Real Estate Investing company needs a business card design

We need a business card design for new Real Estate Investment Company called "Maple Ridge Ventures, LLC." We buy homes for cash and close quickly in any situation. Our company provides an easy and fast option for home owners who are in tough situations who need to sell their home fast and don't want realtor fees or other listing hassles. We also renovate and resell our homes which helps provide housing for the community. We would like to see designs that use the colors blue and white to match our company logo or other colors that may match our company logo. The final design should communicate trust and easy process.
Industry/Entity Type
Business
Contact Information for Business Card
Front should have company name and company logo. back of card should have company logo and area to list services.
Look and feel

```html
<!DOCTYPE html>
<html lang="en">
<head>
<meta charset="utf-8">
<title>Maple Ridge Ventures – Business Card</title>
<link rel="stylesheet" href="https://fonts.googleapis.com/css2?family=Roboto:wght@400;700;900&display=swap">
<style>
  :root {
    --canvas-bg: #e9e9e7;
    --brand-blue: #1a6fb5;
    --brand-blue-deep: #0b4f8a;
    --brand-blue-light: #2a86cc;
    --card-white: #ffffff;
    --card-shade: #e4e4e4;
    --text-grey: #4a4a4a;
    --title-grey: #8a8a8a;
    --service-text: #d6e7f6;
  }
  * { box-sizing: border-box; margin: 0; padding: 0; }
  html, body {
    width: 1200px; height: 950px; overflow: hidden;
    background: var(--canvas-bg);
    font-family: "Roboto", Arial, sans-serif;
  }
  .canvas {
    width: 1200px; height: 950px;
    display: flex; flex-direction: column; align-items: center; justify-content: center;
    gap: 50px;
  }
  .card {
    position: relative;
    width: 700px; height: 400px;
    border-radius: 4px;
    box-shadow: 0 6px 18px rgba(0,0,0,0.18);
    overflow: hidden;
  }

  /* Front: contact side */
  .card--contact {
    background: linear-gradient(160deg, var(--card-white) 0%, var(--card-white) 55%, var(--card-shade) 100%);
  }
  .brand-name {
    display: flex; align-items: center; gap: 12px;
    font-weight: 900; letter-spacing: 0.5px; text-transform: uppercase;
    line-height: 1;
  }
  .brand-name__mark {
    width: 14px; height: 14px; flex: none;
  }
  .card--contact .brand-name {
    position: absolute; left: 48px; top: 52px;
    color: var(--brand-blue); font-size: 36px;
  }
  .card--contact .brand-name__mark { background: var(--brand-blue); }
  .contact-list {
    position: absolute; left: 48px; top: 142px;
    list-style: none; color: var(--text-grey); font-size: 18px; line-height: 27px;
  }
  .contact-list li { display: flex; align-items: center; gap: 10px; }
  .contact-list .no-icon { padding-left: 0; }
  .contact-icon { width: 17px; height: 17px; flex: none; fill: var(--brand-blue); }
  .person {
    position: absolute; right: 70px; bottom: 62px; text-align: left;
  }
  .person__name { color: var(--brand-blue); font-size: 24px; font-weight: 400; }
  .person__title { color: var(--title-grey); font-size: 19px; margin-top: 2px; }

  /* Back: services side */
  .card--services {
    background: linear-gradient(120deg, var(--brand-blue-deep) 0%, var(--brand-blue) 45%, var(--brand-blue-light) 70%, var(--brand-blue-deep) 100%);
  }
  .card--services .brand-name {
    position: absolute; left: 150px; top: 88px;
    color: var(--card-white); font-size: 38px;
  }
  .card--services .brand-name__mark { background: var(--card-white); }
  .services {
    position: absolute; left: 150px; top: 168px; right: 60px;
    list-style: none; color: var(--service-text); font-size: 16px; line-height: 25px;
  }
</style>
</head>
<body>
<main class="canvas">

  <section class="card card--contact" aria-label="Business card front">
    <div class="brand-name"><span class="brand-name__mark"></span>Maple Ridge Ventures</div>
    <ul class="contact-list">
      <li>4120 Birchwood Lane</li>
      <li>Cedar Falls, NY 11208</li>
      <li>
        <svg class="contact-icon" viewBox="0 0 20 20" aria-hidden="true"><path d="M4 2h3l2 5-2 1.5a11 11 0 0 0 4.5 4.5L13 11l5 2v3a2 2 0 0 1-2 2A15 15 0 0 1 2 4a2 2 0 0 1 2-2z"/></svg>
        555 0147 2290
      </li>
      <li>
        <svg class="contact-icon" viewBox="0 0 20 20" aria-hidden="true"><rect x="5" y="2" width="10" height="5"/><rect x="2" y="7" width="16" height="7" rx="1"/><rect x="5" y="12" width="10" height="6" fill="#fff" stroke="currentColor"/></svg>
        555 0193 4417
      </li>
      <li>
        <svg class="contact-icon" viewBox="0 0 20 20" aria-hidden="true"><path d="M2 4h16v12H2z"/><path d="M2 4l8 7 8-7" fill="none" stroke="#fff" stroke-width="1.6"/></svg>
        daniel@mrventures.com
      </li>
      <li>
        <svg class="contact-icon" viewBox="0 0 20 20" aria-hidden="true"><circle cx="10" cy="10" r="8"/><path d="M2 10h16M10 2c3 3 3 13 0 16M10 2c-3 3-3 13 0 16" fill="none" stroke="#fff" stroke-width="1.2"/></svg>
        www.mrventures.com
      </li>
    </ul>
    <div class="person">
      <p class="person__name">Daniel Harlow</p>
      <p class="person__title">President</p>
    </div>
  </section>

  <section class="card card--services" aria-label="Business card back">
    <div class="brand-name"><span class="brand-name__mark"></span>Maple Ridge Ventures</div>
    <ul class="services">
      <li>We buy homes for cash &amp; close quickly in any situation.</li>
      <li>An easy option for home owners to sell their</li>
      <li>home without realtor fees or other listing hassles.</li>
      <li>We renovate &amp; resell homes</li>
    </ul>
  </section>

</main>
</body>
</html>
```